Infografiken für Rechtsfirma
Zielgruppe
Wir sind eine Rechtsfirma, welche sich mit dem europäischen Recht beschäftigt. Wir bieten Insolvenzen in unterschiedlichen Ländern an. Weiter beraten wir hinsichtlich des Vermögensschutzes. Wir helfen dabei, Vermögenswerte zu sichern. Für unseren Bereich Vermögensschutz benötigen wir eine Grafik, welche die Vorteile unseres Produkts direkt auf einen Blick erkennen lässt. Hierzu habe ich eine Grafik eines großen Mobilfunkherstellers beigefügt. Im gleichen Designe möchten wir diese Grafik haben.
Aufgabenstellung
Ich habe eine PDF-Datei (Vermögensschutz) beigefügt, aus welcher sich die Keyfacts ergeben. Diese müssen grafisch aufbereitet werden.

```html
<!DOCTYPE html>
<html lang="de">
<head>
<meta charset="utf-8">
<title>Vermögensschutz – Vorteile</title>
<link rel="stylesheet" href="https://fonts.googleapis.com/css2?family=Quicksand:wght@500;700&family=Montserrat:wght@900&display=swap">
<style>
  :root {
    --bg: #ffffff;
    --green-title: #8bbd5c;
    --green-light: #a6d686;
    --green-mid: #8ec965;
    --green-deep: #86b95a;
    --text: #1f1f1f;
    --badge: #ffffff;
    --wallet-a: #b4505c;
    --wallet-b: #8e3441;
    --bank-a: #f2f3ef;
    --bank-b: #cfd3cb;
    --cash-a: #86ad6d;
    --cash-b: #5e8a50;
    --pie-a: #d7dcb8;
    --pie-b: #c5e09c;
    --safe-a: #6c756b;
    --safe-b: #474e47;
    --scroll-a: #f5f7f3;
    --scroll-b: #d9e0d6;
    --terminal-a: #5f7a5d;
    --terminal-b: #3f553f;
    --bag-a: #a9c987;
    --bag-b: #7fa65f;
    --coins-a: #ee6a4f;
    --coins-b: #cc4432;
  }
  html, body {
    margin: 0;
    padding: 0;
    overflow: hidden;
    background: var(--bg);
  }
  .canvas {
    position: relative;
    width: 1200px;
    height: 1200px;
    overflow: hidden;
    background: var(--bg);
    font-family: "Quicksand", sans-serif;
  }
  .icon-disc {
    position: absolute;
    border-radius: 50%;
    background: radial-gradient(circle at 50% 60%, var(--green-light) 0%, var(--green-mid) 55%, var(--green-deep) 100%);
  }
  .icon-art {
    position: absolute;
    border-radius: 22px;
  }
  .art-wallet   { background: linear-gradient(150deg, var(--wallet-a), var(--wallet-b)); }
  .art-bank     { background: linear-gradient(160deg, var(--bank-a), var(--bank-b)); }
  .art-cash     { background: linear-gradient(150deg, var(--cash-a), var(--cash-b)); }
  .art-pie      { background: linear-gradient(150deg, var(--pie-a), var(--pie-b)); border-radius: 50%; }
  .art-safe     { background: linear-gradient(150deg, var(--safe-a), var(--safe-b)); }
  .art-scroll   { background: linear-gradient(160deg, var(--scroll-a), var(--scroll-b)); }
  .art-terminal { background: linear-gradient(150deg, var(--terminal-a), var(--terminal-b)); }
  .art-bag      { background: linear-gradient(150deg, var(--bag-a), var(--bag-b)); border-radius: 45%; }
  .art-coins    { background: linear-gradient(150deg, var(--coins-a), var(--coins-b)); }
  .badge {
    position: absolute;
    z-index: 2;
    transform: translate(-50%, -50%);
    font-family: "Montserrat", sans-serif;
    font-weight: 900;
    font-size: 44px;
    color: var(--badge);
    letter-spacing: 1px;
    line-height: 1;
    white-space: nowrap;
  }
  .benefit {
    position: absolute;
    transform: translateX(-50%);
    text-align: center;
    white-space: nowrap;
  }
  .benefit-title {
    margin: 0;
    font-weight: 700;
    font-size: 24px;
    letter-spacing: 2.2px;
    color: var(--green-title);
    line-height: 1;
  }
  .benefit-text {
    margin: 10px 0 0;
    font-weight: 500;
    font-size: 15.5px;
    letter-spacing: 1.3px;
    line-height: 26px;
    color: var(--text);
  }
  .main-heading {
    position: absolute;
    left: 642px;
    top: 440px;
    transform: translateX(-50%);
    margin: 0;
    font-weight: 700;
    font-size: 41px;
    letter-spacing: 3.5px;
    color: var(--green-title);
    line-height: 1;
    white-space: nowrap;
  }
</style>
</head>
<body>
<main class="canvas">

  <!-- Reihe 1 -->
  <div class="icon-disc" style="left:199px;top:93px;width:218px;height:218px">
    <div class="icon-art art-wallet" style="left:32px;top:35px;width:147px;height:122px" role="img" aria-label="3D-Illustration: rote Geldbörse mit Karten"></div>
  </div>
  <span class="badge" style="left:311px;top:262px">100%</span>
  <div class="benefit" style="left:306px;top:316px">
    <h2 class="benefit-title">Anonymität</h2>
    <p class="benefit-text">Keine Rückschlüsse<br>auf Sie möglich</p>
  </div>

  <div class="icon-disc" style="left:523px;top:85px;width:214px;height:214px">
    <div class="icon-art art-bank" style="left:15px;top:43px;width:165px;height:130px" role="img" aria-label="3D-Illustration: weißes Bankgebäude mit Säulen"></div>
  </div>
  <div class="benefit" style="left:633px;top:313px">
    <h2 class="benefit-title">Vermögenssichenung</h2>
    <p class="benefit-text">Immobilien Barvermögen<br>Auto Boot Flugzeug Uhren<br>Kryptowährung Firmenanteile</p>
  </div>

  <div class="icon-disc" style="left:837px;top:90px;width:208px;height:208px">
    <div class="icon-art art-cash" style="left:18px;top:35px;width:153px;height:119px" role="img" aria-label="3D-Illustration: gebündelter Geldschein-Stapel"></div>
  </div>
  <span class="badge" style="left:939px;top:256px">0%</span>
  <div class="benefit" style="left:947px;top:314px">
    <h2 class="benefit-title">Wegzugsbesteuerung</h2>
    <p class="benefit-text">Freiheit</p>
  </div>

  <h1 class="main-heading">Vermögensschutz</h1>

  <!-- Reihe 2 -->
  <div class="icon-disc" style="left:186px;top:500px;width:216px;height:216px">
    <div class="icon-art art-pie" style="left:17px;top:28px;width:166px;height:153px" role="img" aria-label="3D-Illustration: Tortendiagramm"></div>
  </div>
  <span class="badge" style="left:297px;top:678px">0%</span>
  <div class="benefit" style="left:293px;top:728px">
    <h2 class="benefit-title">Gunderwerbssteuer</h2>
    <p class="benefit-text">freie Einbringung</p>
  </div>

  <div class="icon-disc" style="left:517px;top:494px;width:224px;height:224px">
    <div class="icon-art art-safe" style="left:42px;top:51px;width:136px;height:127px" role="img" aria-label="3D-Illustration: grauer Tresor"></div>
  </div>
  <div class="benefit" style="left:635px;top:728px">
    <h2 class="benefit-title">Legal und rechtssicher</h2>
  </div>

  <div class="icon-disc" style="left:853px;top:491px;width:218px;height:218px">
    <div class="icon-art art-scroll" style="left:29px;top:34px;width:160px;height:147px" role="img" aria-label="3D-Illustration: Dokumentrolle mit grünem Haken"></div>
  </div>
  <span class="badge" style="left:962px;top:670px">0%</span>
  <div class="benefit" style="left:970px;top:727px">
    <h2 class="benefit-title">Erbschaftssteuer</h2>
  </div>

  <!-- Reihe 3 -->
  <div class="icon-disc" style="left:171px;top:840px;width:224px;height:224px">
    <div class="icon-art art-terminal" style="left:28px;top:26px;width:170px;height:165px" role="img" aria-label="3D-Illustration: Kartenterminal mit Beleg"></div>
  </div>
  <div class="benefit" style="left:280px;top:1093px">
    <h2 class="benefit-title">Steueroptimierung</h2>
    <p class="benefit-text">für das laufende<br>Einkommen</p>
  </div>

  <div class="icon-disc" style="left:509px;top:835px;width:222px;height:222px">
    <div class="icon-art art-bag" style="left:27px;top:37px;width:170px;height:153px" role="img" aria-label="3D-Illustration: Geldsack mit Münzen"></div>
  </div>
  <div class="benefit" style="left:617px;top:1093px">
    <h2 class="benefit-title">Schutz</h2>
    <p class="benefit-text">vor Ansprüchen<br>Dritter</p>
  </div>

  <div class="icon-disc" style="left:847px;top:842px;width:218px;height:218px">
    <div class="icon-art art-coins" style="left:47px;top:53px;width:126px;height:113px" role="img" aria-label="3D-Illustration: rote Münzstapel"></div>
  </div>
  <span class="badge" style="left:962px;top:1019px">100%</span>
  <div class="benefit" style="left:956px;top:1088px">
    <h2 class="benefit-title">Insolvenz sicher</h2>
    <p class="benefit-text">Kein Zugriff vom<br>Insolvenzverwalter</p>
  </div>

</main>
</body>
</html>
```